VELUNDO Brisbane Tiling Service

My name is Mirko Bostel i need a business card for a new company. We are wall and floor tilers based in Brisbane, our company is Velundio Brisbane Tiling Service.
We would like a logo from our website used on our cards. Our website is www.velundio.com.au

I would like my Facebook and Twitter accounts on my card.

Industry/Entity Type

Business

Colors
0692cd
3176b5
33a6d7
85cae6

```html
<!DOCTYPE html>
<html lang="en">
<head>
<meta charset="utf-8">
<title>Velundio Business Card</title>
<link href="https://fonts.googleapis.com/css2?family=Arimo:wght@400;700&family=Great+Vibes&family=Open+Sans:wght@400&display=swap" rel="stylesheet">
<style>
  :root {
    --blue-bright: #0692cd;
    --blue-mid: #3176b5;
    --blue-sky: #33a6d7;
    --blue-pale: #85cae6;
    --title-blue: #1f5c9c;
    --icon-blue: #2aa5e6;
    --ink: #111111;
    --black: #000000;
    --white: #ffffff;
    --stage-light: #f4f4f4;
    --stage-dark: #d6d6d6;
    --back-blue-centre: #0b62ae;
    --back-blue-edge: #034a86;
    --back-navy-centre: #11305e;
    --back-navy-edge: #061734;
  }
  * { margin: 0; padding: 0; box-sizing: border-box; }
  html, body { width: 1200px; height: 1000px; overflow: hidden; }
  body {
    position: relative;
    background: radial-gradient(ellipse at 50% 40%, var(--stage-light), var(--stage-dark));
    font-family: "Arimo", Arial, sans-serif;
  }
  .card {
    position: absolute;
    overflow: hidden;
    box-shadow: 0 6px 18px rgba(0,0,0,.35);
  }
  .card-front {
    left: 110px; top: 72px; width: 949px; height: 544px;
    background: var(--white);
    border: 1px solid #333;
  }
  .front-curve { position: absolute; left: 0; top: 0; width: 949px; height: 544px; }
  .brand-square {
    position: absolute; left: 47px; top: 45px; width: 82px; height: 82px;
    background: var(--blue-mid);
  }
  .brand-name {
    position: absolute; left: 140px; top: 48px;
    font-family: "Open Sans", sans-serif; font-weight: 400;
    font-size: 64px; line-height: 1; color: var(--blue-bright);
  }
  .person-name {
    position: absolute; left: 45px; top: 160px;
    font-family: "Great Vibes", cursive; font-size: 68px; line-height: 1;
    color: var(--ink);
  }
  .person-title {
    position: absolute; left: 50px; top: 259px;
    font-size: 21px; font-weight: 700; line-height: 1;
    color: var(--title-blue); letter-spacing: 0.3px;
  }
  .contact-line {
    position: absolute; right: 74px;
    font-size: 29px; line-height: 1; color: var(--white); white-space: nowrap;
  }
  .contact-line.strong { font-weight: 700; font-size: 30px; }
  .contact-phone { top: 308px; }
  .contact-email { top: 354px; }
  .contact-facebook { top: 400px; }
  .contact-twitter { top: 445px; }
  .contact-address {
    position: absolute; right: 44px; top: 492px;
    font-size: 21px; font-weight: 700; line-height: 1; color: var(--blue-sky);
    white-space: nowrap;
  }
  .contact-icons { position: absolute; left: 884px; top: 308px; width: 30px; height: 170px; }

  .card-back { top: 654px; width: 561px; height: 321px; border: 1px solid #eee; }
  .card-back-blue { left: 24px; background: radial-gradient(ellipse at 40% 35%, var(--back-blue-centre), var(--back-blue-edge)); }
  .card-back-navy { left: 611px; width: 560px; background: radial-gradient(ellipse at 40% 35%, var(--back-navy-centre), var(--back-navy-edge)); }
  .back-square { position: absolute; left: 52px; top: 108px; width: 96px; height: 96px; background: var(--white); }
  .back-name {
    position: absolute; left: 166px; top: 108px;
    font-family: "Open Sans", sans-serif; font-size: 78px; line-height: 1; color: var(--white);
  }
  .back-web {
    position: absolute; left: 0; right: 0; top: 255px; text-align: center;
    font-size: 18px; font-weight: 700; line-height: 1; color: var(--white);
  }
</style>
</head>
<body>

<section class="card card-front">
  <svg class="front-curve" viewBox="0 0 949 544" aria-hidden="true">
    <defs>
      <linearGradient id="band" x1="0" y1="0" x2="1" y2="0">
        <stop offset="0" stop-color="#1f5fd0"/>
        <stop offset="1" stop-color="#2f9be8"/>
      </linearGradient>
    </defs>
    <path d="M0,494 Q330,245 949,224 L949,253 Q350,272 0,502 Z" fill="url(#band)"/>
    <path d="M0,502 Q350,272 949,253 L949,544 L0,544 Z" fill="#000"/>
  </svg>

  <div class="brand-square"></div>
  <div class="brand-name">velundio</div>

  <div class="person-name">Mirko Bostel</div>
  <div class="person-title">CHIEF EXECUTIVE OFFICER</div>

  <div class="contact-line strong contact-phone">123-4567890</div>
  <div class="contact-line strong contact-email">contact@email.com</div>
  <div class="contact-line contact-facebook">fb.com/velundio</div>
  <div class="contact-line contact-twitter">@velundio</div>
  <div class="contact-address">123 Your Addres, Goes here, City</div>

  <svg class="contact-icons" viewBox="0 0 30 170" aria-hidden="true">
    <g fill="none" stroke="#2aa5e6" stroke-width="2">
      <circle cx="14" cy="16" r="12"/>
      <circle cx="14" cy="61" r="12"/>
      <circle cx="14" cy="106" r="12"/>
      <circle cx="14" cy="151" r="12"/>
    </g>
    <path d="M9,10 l3,-1 l2,4 l-2,1.5 q1.5,3 4,4.5 l1.5,-2 l4,2 l-1,3 q-7,0 -11.5,-12 z" fill="#2aa5e6"/>
    <rect x="7.5" y="56" width="13" height="10" rx="1" fill="#2aa5e6"/>
    <path d="M8,57 l6,5 l6,-5" fill="none" stroke="#000" stroke-width="1.3"/>
  </svg>
</section>

<section class="card card-back card-back-blue">
  <div class="back-square"></div>
  <div class="back-name">velundio</div>
  <div class="back-web">www.velundio.com.au</div>
</section>

<section class="card card-back card-back-navy">
  <div class="back-square"></div>
  <div class="back-name">velundio</div>
  <div class="back-web">www.velundio.com.au</div>
</section>

</body>
</html>
```